Lanternfold Advisory Business Cards

We need a new layout for our business cards. We have a logo already. But we might be interested in only using the Lanternfold portion of the logo. It has been uploaded.

We would like cards that are not overly busy. Clean. Modern. Perhaps a gray color for one side.

On the back, we would like to have the lanternfold part of the logo and "Take the Leap, we've got you!"

Our business provides medics and safety training for corporate clients. Our website is www.lanternfoldadvisoryllc.example.

Industry/Entity Type

Business

Contact Information for Business Card

We want include name, email address, cell phone, main line number, and website URL on the front. Use the following as an example: Dana Kovrin, dana@lanternfoldadvisoryllc.example, 804.321.7788 (cell), 804.432.919, and www.lanternfoldadvisoryllc.example.

Font styles to use
Serif
Sans Serif

Requirements
Must have
• All required information. Back side logo with "Take the leap, we will catch you!"
Nice to have
• If possible, we would like to consider creating a card in a non-standard shape. Perhaps, the shape of a lanternfold. Just interested in understanding the option.

```html
<!DOCTYPE html>
<html lang="en">
<head>
<meta charset="utf-8">
<title>Lanternfold Advisory – Business Card</title>
<link rel="stylesheet" href="https://fonts.googleapis.com/css2?family=Cookie&display=swap">
<style>
  :root {
    --ink: #231f20;
    --band-blue: #134f8a;
    --paper: #ffffff;
    --frame: #2b2b2b;
    --shadow: rgba(60, 60, 60, 0.55);
  }
  html, body {
    margin: 0;
    padding: 0;
    width: 1200px;
    height: 686px;
    overflow: hidden;
    background: var(--paper);
  }
  .card {
    position: relative;
    width: 1200px;
    height: 686px;
    box-sizing: border-box;
    border: 2px solid var(--frame);
    background: var(--paper);
    overflow: hidden;
    font-family: "Cookie", cursive;
  }
  .band {
    position: absolute;
    left: 0;
    width: 100%;
    background: var(--band-blue);
  }
  .band--upper { top: 292px; height: 43px; }
  .band--lower { top: 348px; height: 46px; }
  .band--footer { top: 629px; height: 53px; }
  .band-gap {
    position: absolute;
    left: 5px;
    right: -4px;
    top: 335px;
    height: 13px;
    background: var(--paper);
  }
  .line {
    position: absolute;
    left: 0;
    width: 100%;
    text-align: center;
    color: var(--ink);
    line-height: 1;
    white-space: nowrap;
    text-shadow: 0 0 2px #fff, 3px 3px 3px var(--shadow);
  }
  .brand {
    top: 175px;
    font-size: 64px;
    color: var(--band-blue);
    text-shadow: none;
  }
  .name { top: 306px; font-size: 70px; }
  .phone-main { top: 380px; font-size: 54px; letter-spacing: 2px; }
  .phone-cell { top: 505px; font-size: 54px; letter-spacing: 2px; }
  .email { top: 566px; font-size: 50px; letter-spacing: 1px; }
  .website { top: 632px; font-size: 48px; letter-spacing: 1px; }
</style>
</head>
<body>
  <main class="card">
    <div class="line brand">Lanternfold</div>

    <div class="band band--upper"></div>
    <div class="band-gap"></div>
    <div class="band band--lower"></div>

    <div class="line name">Dana Kovrin</div>
    <div class="line phone-main">804.432.919</div>
    <div class="line phone-cell">804.321.7788</div>
    <div class="line email">dana@lanternfoldadvisoryllc.example</div>

    <div class="band band--footer"></div>
    <div class="line website">www.lanternfoldadvisoryllc.example</div>
  </main>
</body>
</html>
```